Edgy rebranded biz cards KRB

We are rebranding our 20 yr old mortgage company with a new logo and would like cards to compliment our new look.

Target Market(s)

potential home buyers or clients for refinance

Industry/Entity Type

Mortgage Brokerage

Contact Information for Business Card

418 W. Lomita Ave #305
Henderson, NV 89152
702.519.4827 o
702-519-4829 f
www.kestrelridgelending,example
nmls 842019
KRB is an equal housing lender

Font styles to use
Sans Serif

Colors
0455a3
3176b5
0393ce
33a6d7

Requirements
Must have
• space for a photo
Nice to have
• One side with the company info and the other with the person's info

```html
<!DOCTYPE html>
<html lang="en">
<head>
<meta charset="UTF-8">
<title>Kestrel Ridge Lending – Business Cards</title>
<link href="https://fonts.googleapis.com/css2?family=Montserrat:wght@400;600;700&display=swap" rel="stylesheet">
<style>
  :root {
    --brand-blue: #1275c1;
    --deep-blue: #0455a3;
    --band-grey: #808285;
    --paper: #ffffff;
    --stage: #262626;
    --text-light: #ffffff;
    --photo-top: #e9eef4;
    --photo-bottom: #3d5a85;
  }
  * { margin: 0; padding: 0; box-sizing: border-box; }
  html, body { width: 1200px; height: 1015px; overflow: hidden; }
  body {
    background: var(--stage);
    font-family: "Montserrat", Arial, sans-serif;
    position: relative;
  }
  .card {
    position: absolute;
    left: 280px;
    width: 640px;
    height: 366px;
    overflow: hidden;
    box-shadow: 0 10px 30px rgba(0,0,0,.5);
  }
  .card-front { top: 100px; background: var(--brand-blue); color: var(--text-light); }
  .card-back { top: 550px; background: var(--paper); }
  .card-shapes { position: absolute; inset: 0; z-index: 1; }

  .wordmark {
    position: absolute;
    z-index: 2;
    display: flex;
    align-items: center;
    gap: 10px;
    font-weight: 700;
    letter-spacing: 1px;
    text-transform: uppercase;
    line-height: 1.15;
  }
  .wordmark-mark { width: 12px; height: 12px; flex: none; }
  .card-front .wordmark { left: 40px; top: 142px; font-size: 23px; color: var(--text-light); }
  .card-front .wordmark-mark { background: var(--text-light); }
  .card-back .wordmark { right: 40px; top: 58px; font-size: 23px; color: var(--brand-blue); }
  .card-back .wordmark-mark { background: var(--brand-blue); }

  .divider {
    position: absolute;
    left: 300px; top: 40px;
    width: 1px; height: 220px;
    background: rgba(255,255,255,.45);
  }
  .contact-list {
    position: absolute;
    z-index: 2;
    left: 325px; top: 44px;
    list-style: none;
    font-size: 14px;
    line-height: 24px;
  }
  .contact-list li { display: flex; align-items: center; gap: 8px; }
  .contact-list svg { width: 14px; height: 14px; fill: currentColor; flex: none; }
  .address {
    position: absolute;
    left: 347px; top: 160px;
    font-size: 14px;
    line-height: 24px;
    font-style: normal;
  }

  .photo-slot {
    position: absolute;
    z-index: 0;
    left: 90px; top: 50px;
    width: 240px; height: 240px;
    background: linear-gradient(180deg, var(--photo-top) 0%, var(--photo-top) 45%, var(--photo-bottom) 100%);
  }
  .person {
    position: absolute;
    z-index: 2;
    left: 40px; bottom: 22px;
    color: var(--text-light);
  }
  .person-name { font-size: 22px; font-weight: 700; letter-spacing: 1px; text-transform: uppercase; }
  .person-title { font-size: 15px; font-weight: 400; margin-top: 2px; }
  .card-back .contact-list {
    left: auto; right: 40px; top: auto; bottom: 60px;
    color: var(--text-light);
  }
</style>
</head>
<body>

<section class="card card-front" aria-label="Company side">
  <svg class="card-shapes" viewBox="0 0 640 366" aria-hidden="true">
    <polygon points="0,320 390,320 390,366 0,366" fill="var(--band-grey)"/>
    <polygon points="470,300 640,300 640,366 470,366" fill="var(--band-grey)"/>
    <rect x="390" y="290" width="80" height="76" fill="var(--deep-blue)"/>
    <rect x="412" y="308" width="36" height="36" fill="var(--text-light)" role="img" aria-label="Equal housing lender badge"/>
  </svg>

  <div class="wordmark"><span class="wordmark-mark"></span>Kestrel Ridge<br>Lending</div>

  <div class="divider"></div>

  <ul class="contact-list">
    <li><svg viewBox="0 0 24 24"><path d="M6.6 10.8a15 15 0 0 0 6.6 6.6l2.2-2.2c.3-.3.7-.4 1-.2 1.1.4 2.300.6 3.6.6.6 0 1 .4 1 1V20c0 .6-.4 1-1 1A17 17 0 0 1 3 4c0-.6.4-1 1-1h3.5c.6 0 1 .4 1 1 0 1.3.2 2.5.6 3.6.1.3 0 .7-.2 1z"/></svg>702.519.4827</li>
    <li><svg viewBox="0 0 24 24"><path d="M6 3h12v5H6zM4 9h16a2 2 0 0 1 2 2v6h-4v4H6v-4H2v-6a2 2 0 0 1 2-2zm4 7v3h8v-3z"/></svg>702-519-4829</li>
    <li><svg viewBox="0 0 24 24"><path d="M2 5h20v14H2zm2 2v.5l8 5 8-5V7z"/></svg>dana@kestrelridgelending.example</li>
    <li><svg viewBox="0 0 24 24"><path d="M12 2a10 10 0 1 0 0 20 10 10 0 0 0 0-20zm6.9 9h-3a15 15 0 0 0-1.3-5.6A8 8 0 0 1 18.9 11zM12 4c.9 1.2 1.7 3.8 1.9 7h-3.8c.2-3.2 1-5.8 1.900-7zM4.1 13h3a15 15 0 0 0 1.3 5.6A8 8 0 0 1 4.1 13zm3-2h-3a8 8 0 0 1 4.3-5.6A15 15 0 0 0 7.1 11zm3 2h3.8c-.2 3.2-1 5.8-1.9 7-.9-1.2-1.7-3.8-1.9-7zm5.5 5.6a15 15 0 0 0 1.3-5.6h3a8 8 0 0 1-4.3 5.6z"/></svg>www.kestrelridgelending,example</li>
  </ul>

  <address class="address">
    418 W. Lomita Ave #305<br>
    Henderson, NV 89152<br>
    NMLS: 842019
  </address>
</section>

<section class="card card-back" aria-label="Personal side">
  <div class="photo-slot" role="img" aria-label="Portrait photo of the loan officer"></div>

  <svg class="card-shapes" viewBox="0 0 640 366" aria-hidden="true">
    <polygon points="330,218 640,218 640,232 330,232" fill="var(--band-grey)"/>
    <polygon points="0,290 330,290 330,232 640,232 640,366 0,366" fill="var(--brand-blue)"/>
  </svg>

  <div class="wordmark"><span class="wordmark-mark"></span>Kestrel Ridge<br>Lending</div>

  <div class="person">
    <p class="person-name">Marcus Reed</p>
    <p class="person-title">Managing Director</p>
  </div>

  <ul class="contact-list">
    <li><svg viewBox="0 0 24 24"><path d="M6.6 10.8a15 15 0 0 0 6.6 6.6l2.2-2.2c.3-.3.7-.4 1-.2 1.1.4 2.3.6 3.6.6.6 0 1 .4 1 1V20c0 .6-.4 1-1 1A17 17 0 0 1 3 4c0-.6.4-1 1-1h3.5c.6 0 1 .4 1 1 0 1.3.2 2.5.6 3.6.1.3 0 .7-.2 1z"/></svg>044-210 555 019</li>
    <li><svg viewBox="0 0 24 24"><path d="M2 5h20v14H2zm2 2v.5l8 5 8-5V7z"/></svg>info@kestrelmail.example</li>
  </ul>
</section>

</body>
</html>
```